Dog care service needs business card design

Our company is Paws Harbour. We provide care for dogs while their owners are away, either through home visits or a holiday stay in the homes of carefully selected minders. Our existing website & Chatterbook cover should provide all the colour cues for our business cards - namely blues, blondes and grey. We have an existing logo (provided).

www.pawsharbourcare.example.au
www.chatterbook.example/pawsharbourcareau

We wish to clearly communicate our three areas of service "dog minding, home visits, dog walking".

We would like to have the files ready for upload to Printlyne (or similar) for immediate printing.

Target Market(s)

Dog owners who love their dogs like family

Industry/Entity Type

Business

Contact Information for Business Card

Paws Harbour
Ph: 0417 358 904

Font styles to use
Sans Serif

Colors
33a6d7
3176b5

Requirements
Must have
• Logo
• Telephone number
• website
• "Dog minding, home visits, dog walking"
Should not have
• any additional illustrations beyond the logo.

```html
<!DOCTYPE html>
<html lang="en">
<head>
<meta charset="utf-8">
<title>Paws Harbour – Business Cards</title>
<link rel="stylesheet" href="https://fonts.googleapis.com/css2?family=Montserrat:wght@600&family=Questrial&display=swap">
<style>
  :root {
    --page-bg: #e4e4e2;
    --card-white: #ffffff;
    --card-silver: #eeeeee;
    --slate: #3d4350;
    --slate-soft: #4a505c;
    --text-grey: #5a5d63;
    --blue: #33a6d7;
    --blue-deep: #3176b5;
  }
  * { box-sizing: border-box; margin: 0; padding: 0; }
  html, body { width: 1200px; height: 871px; overflow: hidden; }
  body {
    background: var(--page-bg);
    font-family: "Questrial", "Century Gothic", sans-serif;
    position: relative;
  }
  .card {
    position: absolute;
    width: 580px;
    height: 332px;
    border-radius: 3px;
    box-shadow: 0 10px 28px rgba(0,0,0,0.22);
    overflow: hidden;
  }

  /* Back of card: services */
  .card--back {
    left: 80px; top: 90px;
    background: linear-gradient(135deg, #f6f6f6, var(--card-silver));
  }
  .back-mark {
    position: absolute;
    left: 70px; top: 118px;
    display: flex; align-items: center; gap: 12px;
    font-family: "Montserrat", sans-serif;
    font-weight: 600;
    font-size: 30px;
    color: var(--slate);
  }
  .back-mark .dot {
    width: 18px; height: 18px; border-radius: 50%;
    background: var(--blue);
  }
  .services {
    position: absolute;
    left: 372px; top: 112px;
    list-style: none;
    color: var(--text-grey);
    font-size: 19px;
    line-height: 32px;
    letter-spacing: 0.5px;
  }
  .services li { display: flex; align-items: center; gap: 14px; }
  .services svg { width: 14px; height: 12px; flex: none; }

  /* Front of card: contact */
  .card--front {
    left: 540px; top: 460px;
    background: var(--card-white);
  }
  .front-mark {
    position: absolute;
    left: 0; right: 0; top: 58px;
    display: flex; justify-content: center; align-items: center; gap: 14px;
    font-family: "Montserrat", sans-serif;
    font-weight: 600;
    font-size: 40px;
    color: var(--slate);
  }
  .front-mark .dot {
    width: 22px; height: 22px; border-radius: 50%;
    background: var(--blue);
  }
  .business-name {
    position: absolute;
    left: 0; right: 0; top: 150px;
    text-align: center;
    font-family: "Montserrat", sans-serif;
    font-size: 22px;
    font-weight: 600;
    letter-spacing: 1px;
    color: var(--slate-soft);
  }
  .contact {
    position: absolute;
    top: 196px; left: 0; right: 0;
    display: flex; justify-content: center; gap: 48px;
    font-size: 15px;
    color: var(--text-grey);
    letter-spacing: 0.5px;
  }
  .contact span { display: flex; align-items: center; gap: 12px; }
  .contact svg { width: 18px; height: 18px; }
  .social-band {
    position: absolute;
    left: 0; right: 0; bottom: 0;
    height: 62px;
    background: var(--slate);
    display: flex; align-items: center;
    padding-left: 46px; gap: 12px;
    color: #ffffff;
    font-size: 15px;
    letter-spacing: 0.6px;
  }
  .social-band .square {
    width: 22px; height: 22px;
    background: var(--blue-deep);
    border-radius: 2px;
  }
</style>
</head>
<body>

<section class="card card--back" aria-label="Business card back">
  <div class="back-mark"><span class="dot"></span>Paws Harbour</div>
  <ul class="services">
    <li><svg viewBox="0 0 14 12"><path d="M1 6.5 L5 10 L13 1.5" fill="none" stroke="#33a6d7" stroke-width="2.4" stroke-linecap="round" stroke-linejoin="round"/></svg>Dog minding</li>
    <li><svg viewBox="0 0 14 12"><path d="M1 6.5 L5 10 L13 1.5" fill="none" stroke="#33a6d7" stroke-width="2.4" stroke-linecap="round" stroke-linejoin="round"/></svg>home visits</li>
    <li><svg viewBox="0 0 14 12"><path d="M1 6.5 L5 10 L13 1.5" fill="none" stroke="#33a6d7" stroke-width="2.4" stroke-linecap="round" stroke-linejoin="round"/></svg>dog walking</li>
  </ul>
</section>

<section class="card card--front" aria-label="Business card front">
  <div class="front-mark"><span class="dot"></span>Paws Harbour</div>
  <h1 class="business-name">Paws Harbour</h1>
  <div class="contact">
    <span>
      <svg viewBox="0 0 18 18" aria-hidden="true"><path d="M3 7 C3 4 15 4 15 7 L13 8.5 L11.5 6.8 L6.5 6.8 L5 8.5 Z M5 10 H13 L14 15 H4 Z" fill="none" stroke="#33a6d7" stroke-width="1.5" stroke-linejoin="round"/><circle cx="9" cy="12" r="1.6" fill="#33a6d7"/></svg>
      0417 358 904
    </span>
    <span>
      <svg viewBox="0 0 18 18" aria-hidden="true"><circle cx="9" cy="9" r="7.2" fill="none" stroke="#33a6d7" stroke-width="1.5"/><ellipse cx="9" cy="9" rx="3.2" ry="7.2" fill="none" stroke="#33a6d7" stroke-width="1.3"/><path d="M2 9 H16 M3.5 5 H14.5 M3.5 13 H14.5" stroke="#33a6d7" stroke-width="1.2"/></svg>
      www.pawsharbourcare.example.au
    </span>
  </div>
  <footer class="social-band">
    <span class="square" aria-label="Chatterbook"></span>
    www.chatterbook.example/pawsharbourcareau
  </footer>
</section>

</body>
</html>
```